Infographic for Digital Marketing Agency

Infographic or one pager a presentation on a page and a presentation (PowerPoint presentation). We need to represent our "Secret Marketing Formula" with our Marketing Process Plan (5 steps plan and list of our services) and the "Sales funnel" process (see draft attached). Specifications: - We would like to have a graphic up-to-date, modern, dynamic chart related to the digital marketing industry. - For the Secret Formula and the design of our "5 Steps", see the file Infographic-Secret Formula_Content & Infographic-Plan 5 Steps_Content) for the content to be added - and for the Channel Marketing (Funnel Marketing) please see the example attached (file: Infographic-Sales funnel_example) to see the content and the concept (strategies) but do not copy the same design. Need another kind of design to reprocess the flow chart. You can do one big Infographic to represent the 3 or 3 files: - The secret formula of the Web marketing (Secret formula) - The marketing plan in 5 steps (5 steps plan) - The sales channel (the sales funnel process) See 3 documents attached for the content (and see notes in the documents) and our Logo. Our brand must be on all documents. And I'm looking for: https://www.vorlenboard.ca/equipevantix/marketing/ I really like this kind of flow chart: https://www.vorlenboard.ca/pin/918274650391827465/ Content has to be in English on all my designs. Also, all the designs must fit our brand. Http://www.vantixa.ca/ You can use our Website images if you need. Designers can provide other suggestions. And please ask questions if not sure about what I am expected. I also have some others projects coming. Thanks. Gaspard vAntix

Target Market(s)

Marketing director, VP of sales and marketing, Entrepreneurs, Professionals on Health industry, Real estate people

Industry/Entity Type

Marketing

Font styles to use
Sans Serif

Colors

Designer to choose colors to be used in the design.

Requirements
Must have
• Must be in French ... But I provide all the content in my files attached to the brief. Must be the same king of inspirations I provide on the brief. Need something really big in Digital Marketing industry.
Nice to have
• I am looking for: https://www.vorlenboard.ca/equipevantix/marketing/ I really like this kind of flow chart: https://www.vorlenboard.ca/pin/918274650391827465/
Should not have
• Funnel Flow Chart I provide. It's just to present the concept and Flow chart and my content so you can reproduce in a different way.

```html
<!DOCTYPE html>
<html lang="fr">
<head>
<meta charset="utf-8">
<title>Les 5 étapes de votre plan</title>
<link rel="stylesheet" href="https://fonts.googleapis.com/css2?family=Source+Sans+3:wght@400;600;700;800&display=swap">
<style>
  :root {
    --step1: #2b5b9c;
    --step2: #8aad3b;
    --step3: #f6a127;
    --step4: #f26c3b;
    --step5: #a54fd2;
    --ink: #222222;
    --rule: #8c8c8c;
    --chevron: #6c7489;
    --chevron-text: #22252e;
  }
  html, body { margin: 0; padding: 0; overflow: hidden; background: #ffffff; }
  .canvas {
    position: relative; width: 1200px; height: 857px; overflow: hidden;
    background: #ffffff; font-family: "Source Sans 3", sans-serif; color: var(--ink);
  }
  .headline {
    position: absolute; top: 62px; left: 0; width: 100%; margin: 0;
    text-align: center; font-weight: 400; font-size: 30px; letter-spacing: 0.1px; color: #1c1c1c;
  }
  .plan {
    position: absolute; top: 110px; left: 62px; width: 1085px; height: 584px;
    display: grid; grid-template-columns: repeat(5, 1fr);
    border: 1.5px solid var(--rule); box-sizing: border-box;
  }
  .step { position: relative; border-left: 1.5px solid var(--rule); }
  .step:first-child { border-left: none; }
  .step-head {
    height: 100px; display: flex; flex-direction: column; align-items: center;
    color: #ffffff; border-bottom: 1.5px solid var(--rule);
  }
  .step-icon { margin-top: 10px; width: 48px; height: 48px; }
  .step-title {
    margin-top: 4px; font-weight: 700; font-size: 27px; letter-spacing: 0.5px;
    text-decoration: underline; text-decoration-thickness: 2px; text-underline-offset: 3px;
  }
  .step-body { position: relative; height: 482px; }
  .step-label {
    position: absolute; top: 18px; left: 10px;
    writing-mode: vertical-rl; transform: rotate(180deg);
    font-weight: 800; font-size: 27px; letter-spacing: 0.6px; line-height: 1;
  }
  .services { position: absolute; top: 14px; left: 56px; right: 8px; margin: 0; padding: 0; list-style: none; }
  .services li { font-size: 13px; line-height: 17.4px; margin-bottom: 17px; color: #1f1f1f; }
  .step--1 .step-head { background: var(--step1); } .step--1 .step-label { color: var(--step1); }
  .step--2 .step-head { background: var(--step2); } .step--2 .step-label { color: var(--step2); }
  .step--3 .step-head { background: var(--step3); } .step--3 .step-label { color: var(--step3); }
  .step--4 .step-head { background: var(--step4); } .step--4 .step-label { color: var(--step4); }
  .step--5 .step-head { background: var(--step5); } .step--5 .step-label { color: var(--step5); }
  .step--5 .services { left: 56px; }
  .flow { position: absolute; top: 709px; left: 0; width: 1200px; height: 52px; }
  .flow polygon { fill: var(--chevron); }
  .flow text { fill: var(--chevron-text); font-family: "Source Sans 3", sans-serif; font-weight: 700; font-size: 21px; text-anchor: middle; }
  .brand {
    position: absolute; top: 792px; left: 928px; height: 38px;
    display: flex; align-items: center; gap: 12px;
  }
  .brand-mark { display: flex; align-items: center; gap: 6px; font-weight: 800; font-size: 26px; color: #1a1a1a; }
  .brand-dot { width: 12px; height: 12px; border-radius: 50%; background: #1a1a1a; }
  .brand-divider { width: 1.5px; height: 34px; background: #9a9a9a; }
  .partner-badge { width: 96px; height: 34px; border-radius: 4px; background: #eef0f3; border: 1px solid #c9ccd3; }
</style>
</head>
<body>
<div class="canvas">
  <h1 class="headline">Donc... Voici les 5 étapes de votre plan à mettre en place!</h1>

  <div class="plan">
    <section class="step step--1">
      <div class="step-head">
        <svg class="step-icon" viewBox="0 0 48 48" aria-hidden="true">
          <circle cx="24" cy="24" r="23" fill="#fff"/>
          <circle cx="17" cy="15" r="4" fill="var(--step1)"/>
          <circle cx="31" cy="17" r="3" fill="var(--step1)"/>
          <circle cx="13" cy="29" r="3" fill="var(--step1)"/>
          <path d="M16 35 Q26 38 34 28" stroke="var(--step1)" stroke-width="2.5" fill="none"/>
          <path d="M31 27 L35 27 L35 31" stroke="var(--step1)" stroke-width="2.5" fill="none"/>
        </svg>
        <div class="step-title">ÉTAPE 1</div>
      </div>
      <div class="step-body">
        <div class="step-label">POSITIONNEMENT</div>
        <ul class="services">
          <li>Boutique, micro site, site Web complet ou “landing pages” modernes et actuels.</li>
          <li>Analyse et structure d’indexation Searchly &amp; Rapport de mots clés en lien avec vos produits/services.</li>
          <li>Progamme de marketing automatique: Convertissez votre site Web en outil de vente.</li>
          <li>Marketing de contenu de présentation.</li>
        </ul>
      </div>
    </section>

    <section class="step step--2">
      <div class="step-head">
        <svg class="step-icon" viewBox="0 0 48 48" aria-hidden="true">
          <circle cx="24" cy="24" r="23" fill="#fff"/>
          <circle cx="16" cy="19" r="4" fill="var(--step2)"/>
          <circle cx="32" cy="19" r="4" fill="var(--step2)"/>
          <circle cx="24" cy="17" r="5" fill="var(--step2)"/>
          <path d="M15 34 Q15 24 24 24 Q33 24 33 34 Z" fill="var(--step2)"/>
          <path d="M9 32 Q9 25 15 25 L17 25 Q13 28 13 32 Z M39 32 Q39 25 33 25 L31 25 Q35 28 35 32 Z" fill="var(--step2)"/>
        </svg>
        <div class="step-title">ÉTAPE 2</div>
      </div>
      <div class="step-body">
        <div class="step-label">VISITEURS</div>
        <ul class="services">
          <li>Marketing de promotions prospects.</li>
          <li>Canal Marketing prospects.</li>
          <li>Marketing de contenu prospects.</li>
          <li>Publicité remarketing prospects.</li>
          <li>Marketing médias sociaux.</li>
          <li>Référencement par liens externes.</li>
          <li>(À venir) Marketing de conférence Web (Webinaire)</li>
        </ul>
      </div>
    </section>

    <section class="step step--3">
      <div class="step-head">
        <svg class="step-icon" viewBox="0 0 48 48" aria-hidden="true">
          <circle cx="24" cy="24" r="23" fill="#fff"/>
          <circle cx="17" cy="15" r="3.5" fill="var(--step3)"/>
          <circle cx="29" cy="14" r="3.5" fill="var(--step3)"/>
          <path d="M11 27 Q11 20 17 20 Q23 20 23 27 Z M23 26 Q23 19 29 19 Q35 19 35 26 Z" fill="var(--step3)"/>
          <circle cx="27" cy="31" r="6" fill="#fff" stroke="var(--step3)" stroke-width="2.5"/>
          <path d="M31 35 L36 40" stroke="var(--step3)" stroke-width="3" stroke-linecap="round"/>
        </svg>
        <div class="step-title">ÉTAPE 3</div>
      </div>
      <div class="step-body">
        <div class="step-label">PROSPECTS</div>
        <ul class="services">
          <li>Canal marketing visiteurs.</li>
          <li>Indexation Searchly</li>
          <li>Marketing de contenu récurrent. (Blogue)</li>
          <li>Répertoires d’affaires &amp; Positionnement local</li>
          <li>Publicité mobile</li>
          <li>Publicité au coût par clics ( PPC Searchly)</li>
          <li>Publicité médias sociaux (Friendora, Workweave, Clipstream, Etc.)</li>
          <li>Publicité bannières Web (Display)</li>
          <li>&nbsp;( À venir) Marketing de ré-engagement</li>
        </ul>
      </div>
    </section>

    <section class="step step--4">
      <div class="step-head">
        <svg class="step-icon" viewBox="0 0 48 48" aria-hidden="true">
          <circle cx="24" cy="24" r="23" fill="#fff"/>
          <circle cx="24" cy="13" r="4" fill="var(--step4)"/>
          <path d="M18 26 Q18 18 24 18 Q30 18 30 26 Z" fill="var(--step4)"/>
          <path d="M24 27 L24 32 M24 32 L14 37 M24 32 L34 37 M24 32 L24 38" stroke="var(--step4)" stroke-width="2"/>
          <circle cx="13" cy="37" r="3" fill="var(--step4)"/>
          <circle cx="35" cy="37" r="3" fill="var(--step4)"/>
          <circle cx="24" cy="39" r="3" fill="var(--step4)"/>
        </svg>
        <div class="step-title">ÉTAPE 4</div>
      </div>
      <div class="step-body">
        <div class="step-label">OPPORTUNITÉS</div>
        <ul class="services">
          <li>Canal Marketing satisfaction client</li>
          <li>Canal Marketing opportunités</li>
          <li>Marketing de contenu clients. (*Upsales)</li>
          <li>Marketing de promotions clients.</li>
          <li>Création de produits Web (Campagne)</li>
          <li>Publicité Web et remarketing clients</li>
        </ul>
      </div>
    </section>

    <section class="step step--5">
      <div class="step-head">
        <svg class="step-icon" viewBox="0 0 48 48" aria-hidden="true">
          <circle cx="24" cy="24" r="23" fill="#fff"/>
          <path d="M12 20 L19 20 L31 13 L31 35 L19 28 L12 28 Z" fill="var(--step5)"/>
          <path d="M15 28 L18 36 L22 36 L20 28 Z" fill="var(--step5)"/>
          <path d="M34 19 Q37 24 34 29 M37 16 Q42 24 37 32" stroke="var(--step5)" stroke-width="2" fill="none"/>
        </svg>
        <div class="step-title">ÉTAPE 5</div>
      </div>
      <div class="step-body">
        <div class="step-label">PROMOTEURS</div>
        <ul class="services">
          <li>Marketing de contenu promoteurs.</li>
          <li>Marketing de références</li>
          <li>Marketing d’affiliation</li>
          <li>Publicité Web et remarketing promoteurs</li>
        </ul>
      </div>
    </section>
  </div>

  <svg class="flow" viewBox="0 0 1200 52" aria-label="Impressions, Incitatif, Offre irrésistible, Maximisation">
    <polygon points="122,0 366,0 390,26 366,52 122,52 146,26"/>
    <polygon points="360,0 580,0 604,26 580,52 360,52 384,26"/>
    <polygon points="594,0 812,0 836,26 812,52 594,52 618,26"/>
    <polygon points="828,0 1062,0 1086,26 1062,52 828,52 852,26"/>
    <text x="253" y="33">Impressions</text>
    <text x="488" y="33">Incitatif</text>
    <text x="732" y="33">Offre irrésistible</text>
    <text x="962" y="33">Maximisation</text>
  </svg>

  <div class="brand">
    <div class="brand-mark"><span class="brand-dot"></span>vAntix</div>
    <div class="brand-divider"></div>
    <div class="partner-badge" role="img" aria-label="Badge partenaire"></div>
  </div>
</div>
</body>
</html>
```